Flyer Design

A flyer to introduce our new business called Smilewagons on Wheels ,we are a mobile dental hygienist service based in the Teesside area of England.We use portable equipment to treat clients where they live or work Since may 2013 in the uk hygienists no longer need to work with a dentist ,therefore clients can now access dental hygiene care without seeing a dentist.We offer scale and polish ,oral hygiene advice .Our colours are pink,green and purple.we would like to stress the importance of a regular professional clean with the convenience of being treated at home

Target Market(s)

over 18 years of age who choose or need to have there scale and polish at home

Industry/Entity Type

Dental

Colors
e34297
9ccb3b
876aae

Requirements
Must have
• ,must have our logo and our contact details tel 07812460395 and email info@smilewagonsonwheels.co.uk
The hygienists names Moira Palfrey and Janet Ruddock
eye catching and colourful ,not to many words,but getting across we are for anyone who chooses or needs their treatment at home
Nice to have
• we would like the logo to be prominent ,our colours are pink ,green and purple .the font easy to read for older people
Should not have
• A lot of writing on the front the page ,

```html
<!DOCTYPE html>
<html lang="en">
<head>
<meta charset="utf-8">
<title>Smilewagons on Wheels – Flyers</title>
<link rel="stylesheet" href="https://fonts.googleapis.com/css2?family=Arimo:wght@400;700&family=Fira+Sans+Condensed:ital,wght@0,500;0,600;0,700;1,700&family=Open+Sans:wght@400;600&display=swap">
<style>
  :root {
    --pink: #d9619f;
    --pink-deep: #e34297;
    --green: #67bb4f;
    --green-soft: #8cc95a;
    --purple: #876aae;
    --white: #ffffff;
    --page: #ffffff;
    --skin-a: #f3d7c6;
    --skin-b: #dcae95;
    --van-a: #f4f4f4;
    --van-b: #c9c9c9;
  }
  * { box-sizing: border-box; margin: 0; padding: 0; }
  html, body { width: 1200px; height: 772px; overflow: hidden; background: var(--page); }
  .canvas { position: relative; width: 1200px; height: 772px; }

  .flyer {
    position: absolute; top: 12px; width: 564px; height: 732px;
    background: var(--white); overflow: hidden;
    box-shadow: 0 0 0 1px #e6e6e6;
    font-family: "Fira Sans Condensed", sans-serif;
  }
  .flyer--front { left: 24px; }
  .flyer--back { left: 614px; }
  .flyer > * { position: absolute; }
  .backdrop { inset: 0; width: 564px; height: 732px; }

  /* front top */
  .photo-area {
    left: 336px; top: 0; width: 228px; height: 280px;
    background: radial-gradient(ellipse at 45% 40%, var(--skin-a), var(--skin-b) 75%);
    border-bottom-left-radius: 60px;
  }
  .van-area {
    border-radius: 26px 70px 18px 18px;
    background: linear-gradient(180deg, var(--van-a), var(--van-b));
  }
  .flyer--front .van-area { left: 24px; top: 200px; width: 360px; height: 160px; }
  .flyer--back .van-area { left: 40px; top: 170px; width: 486px; height: 218px; }

  .headline {
    left: 14px; top: 28px; width: 282px; text-align: center; color: var(--white);
    line-height: 1.1;
  }
  .headline__ask { font-size: 21px; font-weight: 600; }
  .headline__calm { font-size: 40px; font-weight: 700; letter-spacing: .5px; }
  .headline__promise { font-size: 27px; font-weight: 600; }
  .headline__perks { margin-top: 22px; font-size: 21px; font-weight: 500; letter-spacing: .5px; }

  .brand-dot { border-radius: 50%; background: var(--green); }
  .flyer--front .brand-dot { left: 242px; top: 340px; width: 80px; height: 80px; }
  .flyer--back .brand-dot { left: 388px; top: 44px; width: 60px; height: 60px; }

  .brand { text-align: center; font-family: "Arimo", sans-serif; }
  .brand__name { color: var(--pink); font-weight: 400; }
  .brand__tag { color: var(--green); font-weight: 400; }
  .flyer--front .brand { left: 0; width: 564px; top: 432px; }
  .flyer--front .brand__name { font-size: 41px; }
  .flyer--front .brand__tag { font-size: 25px; margin-top: 4px; }
  .flyer--back .brand { left: 296px; width: 250px; top: 112px; }
  .flyer--back .brand__name { font-size: 22px; }
  .flyer--back .brand__tag { font-size: 15px; margin-top: 2px; }

  /* back top */
  .pitch {
    left: 10px; top: 22px; width: 256px; text-align: center; line-height: 1.2; font-weight: 600;
  }
  .pitch__small { color: var(--pink); font-size: 17px; }
  .pitch__big { color: var(--green); font-size: 22px; }
  .divider { left: 277px; top: 34px; width: 2px; height: 116px; background: var(--pink); }

  .team { left: 0; width: 564px; top: 398px; text-align: center; }
  .team__intro { color: var(--green); font-size: 18px; font-weight: 600; }
  .team__title { color: var(--pink); font-size: 25px; font-weight: 700; font-style: italic; letter-spacing: 1px; margin-top: 4px; }
  .team__names { color: var(--green); font-size: 34px; font-weight: 600; margin-top: 6px; }

  /* shared footer */
  .call-badge {
    left: 30px; top: 560px; width: 118px; height: 96px; border-radius: 50%;
    background: var(--pink-deep); color: var(--white);
    display: flex; flex-direction: column; align-items: center; justify-content: center;
    box-shadow: 0 2px 0 rgba(0,0,0,.15);
  }
  .call-badge svg { width: 26px; height: 26px; }
  .call-badge__text { font-family: "Arimo", sans-serif; font-weight: 700; font-size: 24px; line-height: .95; text-align: center; }
  .contact { left: 196px; top: 572px; color: var(--white); }
  .contact__phone { font-size: 52px; font-weight: 700; letter-spacing: 1px; line-height: 1; }
  .contact__email { font-size: 20px; font-weight: 600; margin-top: 4px; }
  .services {
    left: 0; width: 564px; top: 678px; text-align: center; color: var(--white);
    font-family: "Open Sans", sans-serif; font-size: 24px;
  }
</style>
</head>
<body>
<main class="canvas">

  <section class="flyer flyer--front">
    <svg class="backdrop" viewBox="0 0 564 732" aria-hidden="true">
      <path d="M0 0H564V270Q360 296 0 376Z" fill="var(--pink)"/>
      <path d="M150 378Q360 292 564 262V284Q380 306 200 380Z" fill="var(--green)"/>
      <path d="M0 536Q290 572 564 542V732H0Z" fill="var(--pink)"/>
      <path d="M0 552Q290 588 564 558V732H0Z" fill="var(--green)"/>
    </svg>
    <div class="photo-area" role="img" aria-label="Photo of a smiling woman pointing at her teeth"></div>
    <div class="van-area" role="img" aria-label="Illustration of the white mobile dental van"></div>
    <div class="headline">
      <p class="headline__ask">No Time for Dental Care?</p>
      <p class="headline__calm">DON’T WORRY</p>
      <p class="headline__promise">We will come to you</p>
      <p class="headline__perks">Stress Free | Convenient</p>
    </div>
    <div class="brand-dot" aria-hidden="true"></div>
    <div class="brand">
      <p class="brand__name">Smilewagons on Wheels</p>
      <p class="brand__tag">Mobile Dental Hygienists</p>
    </div>
    <div class="call-badge">
      <svg viewBox="0 0 24 24" aria-hidden="true"><path fill="#fff" d="M6.6 10.8a15.1 15.1 0 0 0 6.6 6.6l2.2-2.2c.3-.3.7-.4 1-.2 1.1.4 2.3.6 3.6.6.6 0 1 .4 1 1V20c0 .6-.4 1-1 1A17 17 0 0 1 3 4c0-.6.4-1 1-1h3.5c.6 0 1 .4 1 1 0 1.3.2 2.5.6 3.6.1.3 0 .7-.2 1z"/></svg>
      <span class="call-badge__text">Call<br>now</span>
    </div>
    <div class="contact">
      <p class="contact__phone">07812 460395</p>
      <p class="contact__email">info@smilewagonsonwheels.co.uk</p>
    </div>
    <p class="services">Scale and Polish | Oral Hygiene Advice</p>
  </section>

  <section class="flyer flyer--back">
    <svg class="backdrop" viewBox="0 0 564 732" aria-hidden="true">
      <path d="M0 536Q290 572 564 542V732H0Z" fill="var(--pink)"/>
      <path d="M0 552Q290 588 564 558V732H0Z" fill="var(--green)"/>
    </svg>
    <div class="pitch">
      <p class="pitch__small">Have your teeth</p>
      <p class="pitch__big">professionally cleaned</p>
      <p class="pitch__small">in the comfort of</p>
      <p class="pitch__big">your own home,</p>
      <p class="pitch__big">care home or workspace.</p>
    </div>
    <div class="divider" aria-hidden="true"></div>
    <div class="brand-dot" aria-hidden="true"></div>
    <div class="brand">
      <p class="brand__name">Smilewagons on Wheels</p>
      <p class="brand__tag">Mobile Dental Hygienists</p>
    </div>
    <div class="van-area" role="img" aria-label="Illustration of the white mobile dental van"></div>
    <div class="team">
      <p class="team__intro">Mobile Dental Hygiene Service run by</p>
      <p class="team__title">QUALIFIED DENTAL HYGIENISTS</p>
      <p class="team__names">Moira Palfrey | Janet Ruddock</p>
    </div>
    <div class="call-badge">
      <svg viewBox="0 0 24 24" aria-hidden="true"><path fill="#fff" d="M6.6 10.8a15.1 15.1 0 0 0 6.6 6.6l2.2-2.2c.3-.3.7-.4 1-.2 1.1.4 2.3.6 3.6.6.6 0 1 .4 1 1V20c0 .6-.4 1-1 1A17 17 0 0 1 3 4c0-.6.4-1 1-1h3.5c.6 0 1 .4 1 1 0 1.3.2 2.5.6 3.6.1.3 0 .7-.2 1z"/></svg>
      <span class="call-badge__text">Call<br>now</span>
    </div>
    <div class="contact">
      <p class="contact__phone">07812 460395</p>
      <p class="contact__email">info@smilewagonsonwheels.co.uk</p>
    </div>
    <p class="services">Scale and Polish | Oral Hygiene Advice</p>
  </section>

</main>
</body>
</html>
```